Business Cards, 2 Trifold Brochures
Plumvault
Professional
Darren K. Whitlow
VP Business Development
482 Haverlund Corporate Park
darren@plumvault.example
http://www.plumvault.example
Need two separate tri-fold brochure designs.
Brochure A: Will be handed out to potential customers, should have similar look and feel as our website (www.plumvault.example). Brochure should summarize the benefits of using a remote managed backup solution.
Brochure B: Will be for potential resellers of PlumVault Service. Should summarize benefits of offering a remotely managed backup solution to their customers, creates additional income stream, profit sharing/very lucrative, will increase their marketability , backup solution has huge benefit to customer, how they can easily market to their existing customer base, and that Plumvault will fully train and support them etc.
•256 bit encryption for ultimate security
•Fast online recovery of any version of any protected file
•Easy Installation and setup
•Completely automated offsite-protection
•High speed internet is all that is required.

```html
<!DOCTYPE html>
<html lang="en">
<head>
<meta charset="utf-8">
<title>PlumVault Business Card</title>
<link href="https://fonts.googleapis.com/css2?family=Arimo:wght@400;700&display=swap" rel="stylesheet">
<style>
  :root {
    --bg: #e9e6e1;
    --navy-dark: #0a2352;
    --navy: #17417f;
    --beam: #5d86c4;
    --orange: #f29a16;
    --orange-deep: #e36d0b;
    --gold: #ffd23c;
    --white: #ffffff;
  }
  html, body { margin: 0; padding: 0; }
  body {
    width: 1200px; height: 906px; overflow: hidden;
    background: var(--bg);
    font-family: "Arimo", Arial, sans-serif;
    position: relative;
  }
  .card {
    position: absolute; width: 560px; height: 320px;
    border-radius: 22px; overflow: hidden;
    box-shadow: 0 6px 18px rgba(0,0,0,.25);
    color: var(--white);
  }
  .card-front { left: 150px; top: 80px; }
  .card-back { left: 500px; top: 500px; }
  .card-art { position: absolute; inset: 0; }
  .brand { position: absolute; left: 30px; top: 26px; display: flex; align-items: center; gap: 12px; }
  .brand-mark { width: 40px; height: 40px; background: var(--orange); border-radius: 8px; }
  .brand-name { font-weight: 700; font-size: 40px; color: var(--white); letter-spacing: -0.5px; }
  .person { position: absolute; left: 30px; top: 92px; }
  .person-name { font-size: 21px; color: var(--orange); text-transform: uppercase; margin: 0; font-weight: 400; }
  .person-title { font-size: 14px; margin: 2px 0 0; }
  .contact { position: absolute; left: 30px; top: 150px; font-size: 12px; line-height: 16px; margin: 0; }
  .online { position: absolute; right: 26px; bottom: 14px; font-size: 12px; line-height: 16px; margin: 0; }
  .benefits { position: absolute; left: 34px; top: 60px; margin: 0; padding: 0; list-style: none; }
  .benefits li { display: flex; align-items: center; gap: 12px; font-size: 15px; height: 36px; }
  .benefits li::before { content: ""; width: 14px; height: 14px; border-radius: 3px; background: var(--orange); flex: none; }
  .back-mark { position: absolute; right: 32px; bottom: 58px; width: 44px; height: 44px; background: var(--orange); border-radius: 9px; }
  .web { position: absolute; right: 24px; bottom: 14px; font-size: 21px; font-weight: 700; }
</style>
</head>
<body>
  <section class="card card-front">
    <svg class="card-art" viewBox="0 0 560 320" aria-hidden="true">
      <defs>
        <linearGradient id="navyFront" x1="0" y1="0" x2="1" y2="1">
          <stop offset="0" stop-color="#17417f"/>
          <stop offset="1" stop-color="#0a2352"/>
        </linearGradient>
        <linearGradient id="orangeFront" x1="0" y1="0" x2="1" y2="0">
          <stop offset="0" stop-color="#f7a51d"/>
          <stop offset="1" stop-color="#e36d0b"/>
        </linearGradient>
      </defs>
      <rect width="560" height="320" fill="url(#orangeFront)"/>
      <path d="M0,0 H560 V262 H100 C55,262 18,252 0,236 Z" fill="url(#navyFront)"/>
      <path d="M0,236 C18,252 55,262 100,262 H560" fill="none" stroke="#ffd23c" stroke-width="3"/>
      <polygon points="230,0 330,0 470,150 380,150" fill="#5d86c4" opacity="0.22"/>
      <polygon points="300,0 360,0 540,200 470,200" fill="#5d86c4" opacity="0.12"/>
    </svg>
    <div class="brand"><span class="brand-mark"></span><span class="brand-name">PlumVault</span></div>
    <div class="person">
      <h1 class="person-name">Darren K. Whitlow</h1>
      <p class="person-title">VP Business Development</p>
    </div>
    <p class="contact">482 Haverlund Corporate Park<br>T : 800-555-0147<br>P : 555-301-2264<br>C : 555-301-7719<br>F : 555-301-4482</p>
    <p class="online">Email : darren@plumvault.example<br>Web : www.plumvault.example</p>
  </section>

  <section class="card card-back">
    <svg class="card-art" viewBox="0 0 560 320" aria-hidden="true">
      <defs>
        <linearGradient id="navyBack" x1="0" y1="0" x2="1" y2="1">
          <stop offset="0" stop-color="#17417f"/>
          <stop offset="1" stop-color="#0a2352"/>
        </linearGradient>
        <linearGradient id="orangeBack" x1="0" y1="0" x2="1" y2="0">
          <stop offset="0" stop-color="#f7a51d"/>
          <stop offset="1" stop-color="#e36d0b"/>
        </linearGradient>
      </defs>
      <rect width="560" height="320" fill="url(#orangeBack)"/>
      <path d="M0,0 H560 V150 C470,250 260,285 0,282 Z" fill="url(#navyBack)"/>
      <path d="M0,282 C260,285 470,250 560,150" fill="none" stroke="#ffd23c" stroke-width="3"/>
      <polygon points="200,0 300,0 420,110 330,110" fill="#5d86c4" opacity="0.22"/>
      <polygon points="270,0 330,0 480,140 420,140" fill="#5d86c4" opacity="0.12"/>
    </svg>
    <ul class="benefits">
      <li>256 bit encryption for ultimate security</li>
      <li>Fast online recovery of any version of any protected file</li>
      <li>Easy Installation and setup</li>
      <li>Completely automated offsite-protection</li>
      <li>High speed internet is all that is required.</li>
    </ul>
    <span class="back-mark"></span>
    <span class="web">www.plumvault.example</span>
  </section>
</body>
</html>
```